Word template Letterhead for Australian Law Firm

We are a small law firm based in Manly, NSW, Australia. We have had a new logo designed for us and wish to freshen up the appearance of our letterhead. We require the letterhead to be in a word document that we can type over. This will not be a ‘printed’ letterhead because we send the majority of our correspondence via email. We would like to see a few options. We have attached our previous letterhead as well as the artwork for our new logo. We like the idea of a watermark across the bottom of the letter but the watermark must stay in place and we must be able to type over it. We are open to some colour throughout the letterhead because the majority of our correspondence is sent electronically. We also use electronic signatures. I have uploaded an example of this.The letterhead must include:-1. Our address details – including our phone number, physical address, website address etc. These details can be found on the copy of our previous letterhead;2. ABN Number;3. The words ‘Brevicor (NSW) Pty Ltd ACN 482 731 058 trading as Shipton & AssociatesLiability limited by a scheme approved under Professional Standards Legislation. The letterhead does not need to include the names and qualifications of the people working at the firm. Thank you.

Target Market(s)

Clients and other parties

Industry/Entity Type

Law Firm

Font styles to use
Other font styles liked:
• raleway, montserrat

Colors

Designer to choose colors to be used in the design.

Requirements
Must have
• Certain wording - please see project description.
• Must be a word document and must be able to type over the watermark etc.
Nice to have
• Watermark at the bottom of the letter.

```html
<!DOCTYPE html>
<html lang="en">
<head>
<meta charset="utf-8">
<title>Kervell &amp; Associates Letterhead</title>
<link href="https://fonts.googleapis.com/css2?family=Roboto:wght@400;500&display=swap" rel="stylesheet">
<style>
  :root {
    --backdrop: #e4e4e6;
    --paper: #f4f4f5;
    --ink: #4a4a4f;
    --ink-dark: #2b2b30;
    --rule: #9a9a9e;
    --brand-blue: #3f4a9c;
  }
  * { box-sizing: border-box; margin: 0; padding: 0; }
  html, body {
    width: 1024px;
    height: 1200px;
    overflow: hidden;
    background: var(--backdrop);
    font-family: "Roboto", Arial, sans-serif;
    color: var(--ink);
  }
  .letterhead {
    position: absolute;
    left: 88px;
    top: 0;
    width: 848px;
    height: 1200px;
    background: var(--paper);
  }
  .brand {
    position: absolute;
    left: 80px;
    top: 166px;
    display: flex;
    align-items: center;
    gap: 10px;
  }
  .brand-dot {
    width: 14px;
    height: 14px;
    border-radius: 50%;
    background: var(--brand-blue);
  }
  .brand-name {
    font-weight: 500;
    font-size: 19px;
    letter-spacing: 0.6px;
    color: var(--ink-dark);
  }
  .header-rule {
    position: absolute;
    left: 75px;
    top: 210px;
    width: 699px;
    height: 1px;
    background: var(--rule);
  }
  .contact {
    position: absolute;
    top: 236px;
    font-size: 12px;
    line-height: 16px;
    color: var(--ink);
  }
  .contact-address { left: 76px; text-transform: uppercase; top: 238px; }
  .contact-phone { left: 280px; }
  .contact-online { left: 423px; }
  .contact-abn { right: 74px; top: 252px; }
  .contact-line { display: flex; align-items: center; gap: 6px; }
  .contact-line svg { width: 10px; height: 10px; fill: var(--brand-blue); flex: none; }
  .legal-footer {
    position: absolute;
    left: 0;
    right: 0;
    top: 1100px;
    text-align: center;
    font-size: 11.5px;
    line-height: 15px;
    color: var(--ink);
  }
</style>
</head>
<body>
  <main class="letterhead">
    <div class="brand">
      <span class="brand-dot"></span>
      <span class="brand-name">Kervell &amp; Associates</span>
    </div>

    <div class="header-rule"></div>

    <address class="contact contact-address" style="font-style:normal">
      Suite 4, 12 Harbour<br>Lane, Manly NSW 2095
    </address>

    <div class="contact contact-phone">
      <div class="contact-line">
        <svg viewBox="0 0 10 10" aria-hidden="true"><path d="M2 0.5 L3.6 2.6 L2.7 3.7 C3.3 5 4.7 6.5 6.2 7.2 L7.3 6.3 L9.5 7.9 L8.4 9.5 C4.5 9.3 0.7 5.5 0.5 1.6 Z"/></svg>
        <span>(02) 9481 3370</span>
      </div>
      <div class="contact-line">
        <svg viewBox="0 0 10 10" aria-hidden="true"><path d="M2 0.5 L3.6 2.6 L2.7 3.7 C3.3 5 4.7 6.5 6.2 7.2 L7.3 6.3 L9.5 7.9 L8.4 9.5 C4.5 9.3 0.7 5.5 0.5 1.6 Z"/></svg>
        <span>(02) 9481 3371</span>
      </div>
    </div>

    <div class="contact contact-online">
      <div class="contact-line">
        <svg viewBox="0 0 10 10" aria-hidden="true"><path d="M0.5 2 H9.5 V8.5 H0.5 Z M0.9 2.4 L5 5.6 L9.1 2.4" /></svg>
        <span>reception@brevicorlaw.com.au</span>
      </div>
      <div class="contact-line">
        <svg viewBox="0 0 10 10" aria-hidden="true"><circle cx="5" cy="5" r="4.6"/><path d="M3 2.5 C4 3 3.8 4.2 5 4.5 C6 4.8 5.5 6.5 6.8 7 L6 8.8 C4 8 4.5 6.5 3 6 Z" fill="#f4f4f5"/></svg>
        <span>kervellandassociates.com.au</span>
      </div>
    </div>

    <div class="contact contact-abn">ABN: 31 482 731 058</div>

    <footer class="legal-footer">
      Brevicor (NSW) Pty Ltd ACN 482 731 058 trading as Kervell &amp; Associates<br>
      Liability limited by a scheme approved under Professional Standards Legislation. Legal practitioners at<br>
      Brevicor (NSW) Pty Ltd are members of the scheme.
    </footer>
  </main>
</body>
</html>
```